Swift Heron Parcel & Delivery Services needs a flyer

We need an introductory flyer for a new company based in Yellowknife, Northwest Territories,Canada. Our company name is Swift Heron Parcel & Delivery Services. We will be handling envelopes and small packages up to 20 pounds. We expect 20 percent of our business to come from residential customers and 80 percent from the business community including lawyers, doctors, engineers and government offices. The main message that we will try to convey in this flyer is that we are a new and exciting company that promises to make 100% customer satisfaction our number one goal. I would like the layout to be elegant and simple and certainly not cluttered. It will be a single sided flyer. Text should be easy to read and most likely at most two fonts. I would like one stunning image or photo relating to the courier business and message. There should be plenty of white space throughout the flyer and nice margins on all sides. I would like my flyer to be 8.5 inches by 11 inches and it should read from top to bottom. . I would like a nice big bold headline that in some way mentions " Special Offer- Up to 100% Off. You can change the wording if you have a better idea. Throughout the flyer you can highlight and italicize for emphasis. Please try to use bullet points for my five main reasons for hiring our company which are: you will be 100% satisfied with each delivery or you will be given a complete refund no questions asked, your envelope or package will be delivered on time every time, you will always be treated throughout the delivery process in a professional manner, you will be given the widest selection in Yellowknife of price points and delivery options , you can trust us with your most important and time sensitive deliveries. Try to incorporate something next to these five points to really draw attention like a check mark, star etc.... I would prefer if my company name and contact info is in the bottom third of the flyer. My email is swiftheronparcelyk@mailbox-example.net. My phone number is 867-392-7184. It might be a good idea to have my phone number also at the top of the flyer someplace after the headline saying like Call Now!!! you can use boxes, borders and contrasting bold colors to bring flyer to life. I have a testimonial from a business owner that I dealt with when I ran another business which would be nice to have included . " While receiving daily deliveries for 18 years from Colin Marsh I found him to be punctual , reliable and efficient " Glen Hartley, owner of Hartley and Pruitt Supply LTD, Yellowknife,NWT. I thought perhaps at the top of flyer after the headline perhaps in some way you could say Yellowknife's newest and best courier and delivery service is pleased to offer the following stunning discounts: then you could list the three special offers: 1) First 5 businesses to book regular scheduled deliveries will get 100% off their first delivery. 2) First 5 businesses to book a single delivery will get 50% off that delivery. 3) First 5 residential customers to book a delivery will receive 25% off that delivery. I thought you could mention my name somewhere. Colin Marsh. Owner has lived in Yellowknife for 42 years and has 20 years experience doing performing important and time sensitive deliveries. Perhaps you could mention somewhere that we will have a couple of ongoing discounts also which will be 1) seniors discounts. 2) regular scheduled deliveries discounts. I have suggested colors but if you have other ideas I would certainly look at them. Our business tag line is. On Time Every Time
Target Market(s)
Business owners typically males 30-50 years old
Industry/Entity Type
Delivery Service
Requirements
Must have
- Done in CMYK mode sufficient bleed size for printing
Nice to have
- Nothing set in stone. I recently had my logo design uploaded to this brief. It is up to you if you feel it should be included in the flyer.
Should not have
- I am willing to look at any design

```html
<!DOCTYPE html>
<html lang="en">
<head>
<meta charset="utf-8">
<title>Swift Heron Parcel &amp; Delivery Services — Flyer</title>
<link href="https://fonts.googleapis.com/css2?family=Lato:ital,wght@0,400;0,700;0,900;1,400&display=swap" rel="stylesheet">
<style>
  :root{
    --backdrop:#ebebeb;
    --navy:#1d3a72;
    --navy-deep:#15295a;
    --yellow:#f7ec2a;
    --red:#ec3d55;
    --ink:#1b1b1b;
    --bar:#3a3a32;
    --white:#ffffff;
    --sky-top:#7fb4d8;
    --sky-low:#dfe8ee;
    --ground:#c9cdd1;
  }
  *{box-sizing:border-box;margin:0;padding:0}
  html,body{width:1200px;height:795px;overflow:hidden;background:var(--backdrop);font-family:"Lato",sans-serif}
  .flyer{position:absolute;left:322px;top:37px;width:556px;height:720px;overflow:hidden;background:var(--navy);box-shadow:0 2px 10px rgba(0,0,0,.12)}
  .flyer-shapes{position:absolute;inset:0}
  .hero-photo{position:absolute;left:0;top:0;width:556px;height:300px}
  .brand-box{position:absolute;left:362px;top:44px;width:168px;height:172px;background:var(--yellow);padding:16px 12px;text-align:center}
  .brand-name{font-weight:900;font-size:15px;line-height:1.15;color:var(--red);text-transform:uppercase}
  .offer-kicker{margin-top:18px;font-weight:900;font-size:17px;color:var(--navy)}
  .offer-amount{font-weight:700;font-size:26px;line-height:1;color:var(--red)}
  .content{position:absolute;left:26px;top:318px;width:318px}
  .headline{font-size:22px;font-weight:400;color:var(--red);display:flex;align-items:center;gap:8px}
  .headline svg{flex:none}
  .intro{margin-top:7px;font-size:9.2px;line-height:1.38;color:var(--ink)}
  .reasons{list-style:none;margin-top:7px}
  .reasons li{display:flex;gap:6px;align-items:center;font-size:10px;line-height:1.6;color:var(--red);white-space:nowrap}
  .reasons svg{flex:none}
  .call-bar{position:absolute;left:26px;top:566px;width:316px;height:20px;background:var(--red);display:flex;align-items:center;gap:8px;padding-left:6px;color:var(--white);font-size:12px}
  .call-bar strong{font-weight:900}
  .call-bar .icon{width:18px;height:14px;border-radius:3px;background:var(--white);display:flex;align-items:center;justify-content:center}
  .email{position:absolute;left:26px;top:592px;font-size:10.5px;color:var(--navy-deep)}
  .owner-photo{position:absolute;left:352px;top:458px;width:178px;height:202px;background:linear-gradient(#1a1a1a,#050505);border-radius:70px 70px 0 0;display:flex;align-items:center;justify-content:center;text-align:center;color:var(--white);font-weight:700;font-size:14px;line-height:1.35}
  .owner-bar{position:absolute;left:0;top:660px;width:556px;height:24px;background:var(--bar);color:var(--white);font-size:10.5px;display:flex;align-items:center;padding-left:26px}
  .owner-bar strong{font-weight:900;text-transform:uppercase;margin-right:3px}
</style>
</head>
<body>
<main class="flyer">
  <svg class="flyer-shapes" width="556" height="720" viewBox="0 0 556 720" aria-hidden="true">
    <defs>
      <linearGradient id="heroTones" x1="0" y1="0" x2="0" y2="1">
        <stop offset="0" stop-color="var(--sky-top)"/>
        <stop offset=".35" stop-color="var(--sky-low)"/>
        <stop offset="1" stop-color="var(--ground)"/>
      </linearGradient>
    </defs>
    <polygon points="0,0 556,0 556,300 0,290" fill="url(#heroTones)"/>
    <polygon points="300,0 380,0 556,110 556,160" fill="var(--navy)"/>
    <polygon points="0,290 556,300 556,660 0,660" fill="var(--navy)"/>
    <polygon points="0,300 300,288 556,372 556,660 0,660" fill="var(--yellow)"/>
  </svg>

  <div class="hero-photo" role="img" aria-label="Photo of a businessman standing at the tip of a large arrow on a pale floor, with a wrapped cardboard parcel in front"></div>

  <aside class="brand-box">
    <p class="brand-name">Swift Heron Parcel &amp; Delivery Services</p>
    <p class="offer-kicker">SPECIAL OFFER</p>
    <p class="offer-amount">Up to 100%<br>Off</p>
  </aside>

  <section class="content">
    <h1 class="headline">
      <svg width="10" height="14" viewBox="0 0 10 14"><polyline points="2,1 8,7 2,13" fill="none" stroke="var(--red)" stroke-width="2.5"/></svg>
      We fight for your rights!
    </h1>
    <p class="intro">Yellowknife's newest courier, <em>On Time Every Time.</em> Opening offers: first 5 businesses booking regular deliveries get 100% off their first delivery; first 5 single-delivery businesses get 50% off; first 5 residential customers get 25% off. “Punctual, reliable and efficient” — Glen Hartley, Hartley and Pruitt Supply LTD.</p>
    <ul class="reasons">
      <li><svg width="10" height="9" viewBox="0 0 10 9"><polyline points="1,5 4,8 9,1" fill="none" stroke="var(--red)" stroke-width="2"/></svg>100% satisfied or a full refund, no questions asked.</li>
      <li><svg width="10" height="9" viewBox="0 0 10 9"><polyline points="1,5 4,8 9,1" fill="none" stroke="var(--red)" stroke-width="2"/></svg>Delivered on time, every time.</li>
      <li><svg width="10" height="9" viewBox="0 0 10 9"><polyline points="1,5 4,8 9,1" fill="none" stroke="var(--red)" stroke-width="2"/></svg>Professional service through every step.</li>
      <li><svg width="10" height="9" viewBox="0 0 10 9"><polyline points="1,5 4,8 9,1" fill="none" stroke="var(--red)" stroke-width="2"/></svg>Widest choice of prices and delivery options.</li>
      <li><svg width="10" height="9" viewBox="0 0 10 9"><polyline points="1,5 4,8 9,1" fill="none" stroke="var(--red)" stroke-width="2"/></svg>Trusted with your most urgent deliveries.</li>
    </ul>
  </section>

  <div class="call-bar">
    <span class="icon"><svg width="10" height="10" viewBox="0 0 24 24"><path d="M6.6 10.8a15 15 0 006.6 6.6l2.2-2.2c.3-.3.7-.4 1-.2 1.1.4 2.3.6 3.6.6.6 0 1 .4 1 1V20c0 .6-.4 1-1 1A17 17 0 013 4c0-.6.4-1 1-1h3.5c.6 0 1 .4 1 1 0 1.3.2 2.5.6 3.6.1.3 0 .7-.2 1z" fill="var(--red)"/></svg></span>
    <span>CALL US: <strong>867-392-7184</strong></span>
  </div>
  <p class="email">swiftheronparcelyk@mailbox-example.net</p>

  <div class="owner-photo" role="img" aria-label="Placeholder for a photo of the owner">Owner<br>Photo<br>Here!</div>

  <p class="owner-bar"><strong>Colin Marsh</strong>. The Owner has lived in Yellowknife for 42 years and has 20 years experience.</p>
</main>
</body>
</html>
```